Fitness competition business needs a card design

I need a professional business card design using my logo. The card will be horizontal with rounded edges.

Target Market(s)

Female fitness competitors

Industry/Entity Type

Fitness

Contact Information for Business Card

Rose-Lynn Darby
Owner
stagevarno.com
555.301.2187
info@stagevarno.com

Font styles to use
Serif

Colors

Designer to choose colors to be used in the design.

Requirements
Must have
• On the back please add the following:
• Figure
• Bikini
• Physique
• Fitness
Nice to have
• Looking for a very sleek design, contemporary and easy to read.
Should not have
• Should not be difficult to read or be too busy

```html
<!DOCTYPE html>
<html lang="en">
<head>
<meta charset="utf-8">
<title>Stage Varno — Business Card</title>
<link href="https://fonts.googleapis.com/css2?family=Roboto:ital,wght@0,400;0,500;0,700;1,400&family=Roboto+Condensed:wght@700&display=swap" rel="stylesheet">
<style>
  :root {
    --page: #2b2b2d;
    --card-dark: #1d1d1f;
    --card-dark-2: #252527;
    --paper: #f7f7f7;
    --red: #d8231d;
    --grey: #55575b;
    --mark-grey: #6a6a6d;
    --white: #ffffff;
    --muted: #cfcfcf;
  }
  * { box-sizing: border-box; margin: 0; padding: 0; }
  html, body { width: 799px; height: 1200px; overflow: hidden; }
  body {
    background: var(--page);
    font-family: "Roboto", Arial, sans-serif;
    position: relative;
  }
  .card {
    position: absolute;
    left: 80px;
    width: 640px;
    height: 366px;
    border-radius: 28px;
    overflow: hidden;
    background: linear-gradient(135deg, var(--card-dark-2), var(--card-dark));
    box-shadow: 0 18px 40px rgba(0,0,0,0.45);
  }
  .card--front { top: 150px; }
  .card--back { top: 690px; }

  .tagline {
    font-family: "Roboto Condensed", "Arial Narrow", sans-serif;
    font-weight: 700;
    text-transform: uppercase;
    color: var(--white);
    font-size: 20px;
    letter-spacing: 0.2px;
    white-space: nowrap;
  }
  .tagline .sep { color: var(--red); margin: 0 6px; }

  /* Front */
  .front-brand {
    position: absolute;
    left: 0; right: 0; top: 120px;
    text-align: center;
    font-family: "Roboto", Arial, sans-serif;
    font-weight: 700;
    font-size: 56px;
    letter-spacing: 4px;
    color: var(--mark-grey);
    text-transform: uppercase;
  }
  .card--front .tagline {
    position: absolute;
    left: 0; right: 0; top: 262px;
    text-align: center;
  }

  /* Back */
  .back-art { position: absolute; inset: 0; }
  .holder {
    position: absolute;
    left: 40px; top: 34px;
    color: var(--white);
  }
  .holder__name { font-weight: 700; font-size: 24px; }
  .holder__role { font-style: italic; font-size: 14px; color: var(--muted); margin-top: 2px; }
  .contacts {
    position: absolute;
    left: 40px; top: 140px;
    list-style: none;
    color: var(--white);
    font-size: 16px;
  }
  .contacts li { display: flex; align-items: center; gap: 12px; height: 24px; }
  .contacts svg { width: 16px; height: 16px; flex: none; }
  .card--back .tagline {
    position: absolute;
    left: 32px; top: 253px;
    font-size: 19px;
  }
  .back-brand {
    position: absolute;
    left: 400px; right: 12px; top: 118px;
    text-align: center;
    font-family: "Roboto", Arial, sans-serif;
    font-weight: 700;
    font-size: 42px;
    line-height: 1.05;
    color: var(--red);
    text-transform: uppercase;
  }
</style>
</head>
<body>

  <section class="card card--front" aria-label="Card front">
    <div class="front-brand">Stage Varno</div>
    <p class="tagline">Figure<span class="sep">|</span>Bikini<span class="sep">|</span>Physique<span class="sep">|</span>Fitness</p>
  </section>

  <section class="card card--back" aria-label="Card back">
    <svg class="back-art" viewBox="0 0 640 366" preserveAspectRatio="none" aria-hidden="true">
      <rect x="0" y="240" width="420" height="46" fill="var(--red)"/>
      <path d="M412 0 C 365 120, 350 240, 372 366 L640 366 L640 0 Z" fill="var(--red)"/>
      <path d="M426 0 C 380 120, 365 240, 387 366 L640 366 L640 0 Z" fill="var(--paper)"/>
    </svg>

    <div class="holder">
      <h1 class="holder__name">Rose-Lynn Darby</h1>
      <p class="holder__role">Owner</p>
    </div>

    <ul class="contacts">
      <li>
        <svg viewBox="0 0 16 16"><circle cx="8" cy="8" r="7.5" fill="none" stroke="#fff" stroke-width="1"/><path d="M5.5 4.5l1.5 0 0.6 2-1 0.8a5 5 0 0 0 2.1 2.1l0.8-1 2 0.6 0 1.5c-3.5 0.3-6.3-2.5-6-6z" fill="#fff"/></svg>
        <span>555.301.2187</span>
      </li>
      <li>
        <svg viewBox="0 0 16 16"><circle cx="8" cy="8" r="7.5" fill="none" stroke="#fff" stroke-width="1"/><circle cx="8" cy="8" r="4" fill="none" stroke="#fff" stroke-width="1"/><path d="M4 8h8M8 4c-1.8 2.2-1.8 5.8 0 8M8 4c1.8 2.2 1.8 5.8 0 8" fill="none" stroke="#fff" stroke-width="0.8"/></svg>
        <span>www.stagevarno.com</span>
      </li>
      <li>
        <svg viewBox="0 0 16 16"><circle cx="8" cy="8" r="7.5" fill="none" stroke="#fff" stroke-width="1"/><rect x="4" y="5.2" width="8" height="5.6" fill="none" stroke="#fff" stroke-width="1"/><path d="M4 5.4l4 3 4-3" fill="none" stroke="#fff" stroke-width="1"/></svg>
        <span>info@stagevarno.com</span>
      </li>
    </ul>

    <p class="tagline">Figure<span class="sep">|</span>Bikini<span class="sep">|</span>Physique<span class="sep">|</span>Fitness</p>

    <div class="back-brand">Stage<br>Varno</div>
  </section>

</body>
</html>
```